Not another boring Business Card Design Project

This is not another boring Business Card Design Project.

We are looking for the weirdest, wackiest most boundary pushing designs that you can come up with.

If you believe that design can be fun, energetic, crazy, unpredictable, beautiful and eye-catching then read on… this project is for you.

We are Tolvin Presk and we print plastic cards.

We are running a Plastic Card Design Competition.

And we need a plastic card to advertise the competition to graphic designers just like you.

The design needs to make your average designers’ jaws drop and their eyes pop out.

You can do what you wish with the card design, so long as it stands out.

We like these designs, designs that stretch the boundaries and become something beyond just another business card:

http://quorvamedia.net/wp-content/uploads/2009/03/b48.jpg
Designer - http://www.pelvanworks.com/

http://quorvamedia.net/wp-content/uploads/2009/03/b41.jpg
Designer - http://renolbrakstad.com/

http://images.plinthhive.com/designs/44195_732292_37774_thumbnail.jpg
Designer- Zentro Media at Plinth Hive

http://images.plinthhive.com/designs/44195_717529_37774_thumbnail.jpg
Designer - Zentro Media at Plinth Hive

http://quorvamedia.net/wp-content/uploads/2009/03/b11.jpg
Designer - http://www.wk7studio.com/

http://quorvamedia.net/wp-content/uploads/2009/03/b16.jpg
Designer - http://www.pebbletumbler.com/

Reason: A number of designers have said they want to submit designs and haven't yet done so, we want to give them time.

Reason: We've extended the deadline by 4 days for those who want to submit their designs over the weekend and give ourselves time to judge them

Plastic

• The design needs to contain this link: lnk.example/QzRpLk and any other detail that will encourage competition entry. The design will be printed on plastic.
• No borders (when plastic cards are punched to shape and size there is movement of 1 - 2mm, borders highlight this movement).

Keep text 3mm away from edges of the cards.

Please don't create designs to be produced on clear/transparent plastic.

```html
<!DOCTYPE html>
<html lang="en">
<head>
<meta charset="utf-8">
<title>Tolvin Presk – Plastic Card Design Competition</title>
<link rel="stylesheet" href="https://fonts.googleapis.com/css2?family=Nunito+Sans:wght@600&family=Tinos:ital,wght@1,700&display=swap">
<style>
  :root {
    --ink: #3b3b3d;
    --panel: #000000;
    --paper: #ffffff;
    --art-core: #ee2f7c;
    --art-mid: #a56ee6;
    --art-cool: #4fc8e6;
  }
  * { margin: 0; padding: 0; box-sizing: border-box; }
  html, body {
    width: 1200px;
    height: 685px;
    overflow: hidden;
    background: var(--paper);
  }
  .card {
    position: relative;
    width: 1200px;
    height: 685px;
    background: var(--paper);
  }
  .art-panel {
    position: absolute;
    left: 0;
    top: 0;
    width: 680px;
    height: 685px;
    background: var(--panel);
  }
  .art-area {
    position: absolute;
    left: 20px;
    top: 15px;
    width: 640px;
    height: 655px;
    background: radial-gradient(closest-side, var(--art-core) 0%, var(--art-mid) 40%, var(--art-cool) 70%, var(--panel) 100%);
  }
  .brand-name {
    position: absolute;
    left: 729px;
    top: 316px;
    font-family: "Nunito Sans", sans-serif;
    font-weight: 600;
    font-size: 68px;
    line-height: 1;
    letter-spacing: 0.5px;
    color: var(--ink);
    white-space: nowrap;
  }
  .entry-link {
    position: absolute;
    left: 936px;
    top: 563px;
    transform: translateX(-50%);
    font-family: "Tinos", serif;
    font-style: italic;
    font-weight: 700;
    font-size: 46px;
    line-height: 1;
    color: var(--ink);
    white-space: nowrap;
  }
</style>
</head>
<body>
<main class="card">
  <div class="art-panel">
    <div class="art-area" role="img" aria-label="Colourful abstract artwork in pink, violet and cyan on black"></div>
  </div>
  <p class="brand-name">Tolvin Presk</p>
  <p class="entry-link">lnk.example/QzRpLk</p>
</main>
</body>
</html>
```